KB Rubbish Removal Business Card

Hey,
I need a double sided business card designed for a rubbish removal business based in Australia. Logo is already chosen, similar colours preferred for both sides of the business card.

Details to include:

Front:

KB Rubbish Removal
Darren Holloway
Managing Director
Mobile: 0471 902 146
Email: darren@kbrubbishremoval.com.au
Website: kbrubbishremoval.com.au

Rear:

How did we do?
kbrubbishremoval.com.au/review

```html
<!DOCTYPE html>
<html lang="en">
<head>
<meta charset="utf-8">
<title>KB Rubbish Removal Business Card</title>
<link rel="stylesheet" href="https://fonts.googleapis.com/css2?family=Montserrat:wght@400;500;600;700&display=swap">
<style>
  :root {
    --backdrop: #3bbe42;
    --charcoal: #4d4d4d;
    --ink: #333333;
    --paper: #ffffff;
    --brand-green: #3bbe42;
  }
  * { box-sizing: border-box; margin: 0; padding: 0; }
  html, body { width: 1200px; height: 1200px; overflow: hidden; }
  body {
    background: var(--backdrop);
    font-family: "Montserrat", Arial, sans-serif;
    position: relative;
  }
  .card {
    position: absolute;
    left: 228px;
    width: 743px;
    height: 424px;
    overflow: hidden;
  }
  .card--front { top: 150px; background: var(--paper); }
  .card--back { top: 625px; background: var(--charcoal); }

  .front__panel {
    position: absolute; left: 0; top: 0;
    width: 310px; height: 100%;
    background: var(--charcoal);
  }
  .front__stripe {
    position: absolute;
    width: 12px;
    background: var(--brand-green);
  }
  .front__stripe--top { left: 311px; top: 0; height: 244px; }
  .front__stripe--bottom { left: 317px; top: 326px; height: 98px; }

  .brand-lockup {
    position: absolute;
    display: flex; flex-direction: column; align-items: center;
    gap: 14px;
    transform: translate(-50%, -50%);
    text-align: center;
  }
  .brand-lockup__dot {
    width: 64px; height: 64px; border-radius: 50%;
    background: var(--brand-green);
  }
  .brand-lockup__name {
    color: var(--brand-green);
    font-weight: 700;
    font-size: 22px;
    line-height: 1.2;
    width: 200px;
  }
  .card--front .brand-lockup { left: 162px; top: 213px; }
  .card--back .brand-lockup { left: 371px; top: 194px; }

  .front__company {
    position: absolute; left: 365px; top: 60px;
    font-size: 29px; font-weight: 700; color: var(--ink);
  }
  .front__name {
    position: absolute; left: 365px; top: 173px;
    font-size: 24px; font-weight: 600; color: var(--ink);
    letter-spacing: 1px; text-transform: uppercase;
  }
  .front__role {
    position: absolute; left: 365px; top: 199px;
    font-size: 16px; font-weight: 400; color: var(--ink);
  }
  .contact-list { list-style: none; }
  .contact-item {
    position: absolute; left: 366px;
    display: flex; align-items: center; gap: 12px;
    font-size: 16px; color: var(--ink);
    transform: translateY(-50%);
  }
  .contact-item:nth-child(1) { top: 262px; }
  .contact-item:nth-child(2) { top: 304px; }
  .contact-item:nth-child(3) { top: 346px; }
  .contact-item__icon {
    width: 23px; height: 23px;
    background: var(--brand-green);
    display: flex; align-items: center; justify-content: center;
  }
  .contact-item__icon svg { width: 15px; height: 15px; }

  .back__review {
    position: absolute; left: 0; right: 0; top: 340px;
    text-align: center; color: var(--paper);
    font-size: 18px; font-weight: 600; line-height: 26px;
  }
</style>
</head>
<body>

<section class="card card--front">
  <div class="front__panel"></div>
  <div class="front__stripe front__stripe--top"></div>
  <div class="front__stripe front__stripe--bottom"></div>

  <div class="brand-lockup">
    <span class="brand-lockup__dot"></span>
    <span class="brand-lockup__name">KB Rubbish Removal</span>
  </div>

  <h1 class="front__company">KB Rubbish Removal</h1>
  <p class="front__name">Darren Holloway</p>
  <p class="front__role">Managing Director</p>

  <ul class="contact-list">
    <li class="contact-item">
      <span class="contact-item__icon">
        <svg viewBox="0 0 16 16" fill="none" stroke="#fff" stroke-width="1.5" stroke-linecap="round" stroke-linejoin="round">
          <path d="M4 2.5l2 .5 1 3-1.5 1a7 7 0 0 0 3.5 3.5l1-1.5 3 1 .5 2c-1 1-2.5 1.5-4 1A9 9 0 0 1 3 6.5C2.5 5 3 3.5 4 2.5z"/>
        </svg>
      </span>
      <span>0471 902 146</span>
    </li>
    <li class="contact-item">
      <span class="contact-item__icon">
        <svg viewBox="0 0 16 16" fill="none" stroke="#fff" stroke-width="1.5" stroke-linejoin="round">
          <rect x="2" y="4" width="12" height="8"/>
          <path d="M2 4l6 5 6-5"/>
        </svg>
      </span>
      <span>darren@kbrubbishremoval.com.au</span>
    </li>
    <li class="contact-item">
      <span class="contact-item__icon">
        <svg viewBox="0 0 16 16" fill="none" stroke="#fff" stroke-width="1.2">
          <circle cx="8" cy="8" r="6"/>
          <ellipse cx="8" cy="8" rx="2.6" ry="6"/>
          <path d="M2 8h12M3 5h10M3 11h10"/>
        </svg>
      </span>
      <span>kbrubbishremoval.com.au</span>
    </li>
  </ul>
</section>

<section class="card card--back">
  <div class="brand-lockup">
    <span class="brand-lockup__dot"></span>
    <span class="brand-lockup__name">KB Rubbish Removal</span>
  </div>
  <p class="back__review">How did we do?<br>kbrubbishremoval.com.au/review</p>
</section>

</body>
</html>
```